Business Card Design for Brightkeel

The company provides engineering tender consulting services and personnel resources. The target market is large engineering construction and services companies. The business is based in Australia.

```html
<!DOCTYPE html>
<html lang="en">
<head>
<meta charset="utf-8">
<title>Brightkeel Business Cards</title>
<link rel="stylesheet" href="https://fonts.googleapis.com/css2?family=Open+Sans:wght@400;700&display=swap">
<style>
  :root {
    --page: #ffffff;
    --brand-blue: #0a64b4;
    --card-blue: #0b77b3;
    --sky-blue: #2ea3e0;
    --pale-blue: #c3e0ee;
    --faint-blue: #3f93c6;
    --mark-grey: #8f9193;
    --swoosh-dark: #3b3b3d;
    --text-grey: #4a4a4a;
    --card-white: #fdfdfd;
  }
  * { box-sizing: border-box; margin: 0; padding: 0; }
  html, body {
    width: 1200px; height: 800px; overflow: hidden;
    background: var(--page);
    font-family: "Open Sans", Arial, sans-serif;
  }
  .sheet { position: relative; width: 1200px; height: 800px; }
  .card {
    position: absolute; width: 516px; height: 298px; overflow: hidden;
    background: var(--card-white);
    box-shadow: 3px 4px 6px rgba(0,0,0,0.28);
  }
  .card--front { left: 53px; top: 87px; }
  .card--back-light { left: 625px; top: 87px; }
  .card--back-blue { left: 305px; top: 406px; background: var(--card-blue); }

  .wave { position: absolute; left: 0; top: 0; width: 516px; height: 298px; }

  .holder-name {
    position: absolute; right: 14px; top: 26px;
    color: #ffffff; font-size: 19px; font-weight: 400;
  }

  .wordmark {
    position: absolute; display: flex; align-items: center; gap: 10px;
    font-family: "Open Sans", Arial, sans-serif;
    font-weight: 700; font-size: 40px; letter-spacing: -1.5px; line-height: 1;
    color: var(--brand-blue);
  }
  .wordmark__square { width: 22px; height: 22px; background: var(--mark-grey); flex: none; }
  .card--front .wordmark { left: 30px; top: 172px; }
  .card--back-light .wordmark { left: 140px; top: 124px; }
  .card--back-blue .wordmark { left: 140px; top: 158px; color: #ffffff; }
  .card--back-blue .wordmark__square { background: #ffffff; }

  .decor-square { position: absolute; width: 104px; height: 132px; border-radius: 18px; }
  .card--back-light .decor-square { left: 14px; top: 115px; background: var(--pale-blue); }
  .card--back-blue .decor-square { left: 18px; top: 142px; background: var(--faint-blue); }

  .contact {
    position: absolute; right: 14px; top: 212px; text-align: right;
    font-size: 15px; line-height: 19px; color: var(--text-grey);
  }
  .contact__label { color: var(--sky-blue); margin-right: 3px; }
  .contact__web { color: var(--sky-blue); line-height: 16px; }
</style>
</head>
<body>
<main class="sheet">

  <section class="card card--front">
    <svg class="wave" viewBox="0 0 516 298" aria-hidden="true">
      <defs>
        <linearGradient id="band" x1="0" y1="0" x2="1" y2="0">
          <stop offset="0" stop-color="#2a5fb8"/>
          <stop offset="1" stop-color="#2fa6e2"/>
        </linearGradient>
        <linearGradient id="swoosh" x1="0" y1="0" x2="1" y2="0">
          <stop offset="0" stop-color="#9a9a9c"/>
          <stop offset="0.45" stop-color="#2f2f31"/>
          <stop offset="1" stop-color="#6b6b6d"/>
        </linearGradient>
      </defs>
      <path d="M0,0 H516 V140 C410,92 250,34 0,38 Z" fill="url(#band)"/>
      <path d="M0,40 C250,36 410,96 516,146 L516,154 C410,106 250,50 0,50 Z" fill="url(#swoosh)"/>
    </svg>
    <p class="holder-name">Your Name</p>
    <div class="wordmark"><span class="wordmark__square"></span>Brightkeel</div>
    <div class="contact">
      <p><span class="contact__label">p</span>+00 (0)0 0000 0000</p>
      <p><span class="contact__label">m</span>+00 (0)0 0000 0000</p>
      <p><span class="contact__label">e</span>your@brightkeel.com</p>
      <p class="contact__web">www.brightkeel.com</p>
    </div>
  </section>

  <section class="card card--back-light">
    <span class="decor-square"></span>
    <div class="wordmark"><span class="wordmark__square"></span>Brightkeel</div>
  </section>

  <section class="card card--back-blue">
    <span class="decor-square"></span>
    <div class="wordmark"><span class="wordmark__square"></span>Brightkeel</div>
  </section>

</main>
</body>
</html>
```